Pathways to Brightmoor Land Ventures

size of the ad - 8”x 10.75" plus 0.25" bleed
I would like an ad for a magazine that will stand out and make people want to read the ad.
The ad should not be crowded and people reading the ad will be able to read the text.
I would like it to be a creative and modern-day design.
the list of topics should not be the focus of the ad.
the text is attached.
If you decide to use people in the ad then please no ladies.
please note that leave over 1 inch for the bottom of the footer

```html
<!DOCTYPE html>
<html lang="en">
<head>
<meta charset="utf-8">
<title>Real Estate Course Flyer</title>
<link href="https://fonts.googleapis.com/css2?family=Montserrat:wght@400;500;700;800&display=swap" rel="stylesheet">
<style>
  :root{
    --red:#c8203f;
    --navy:#1f2f6b;
    --ink:#1a1a1a;
    --label:#2b3566;
    --paper:#ffffff;
    --stage:#e4e4e4;
    --icon-ring:#ececec;
  }
  *{margin:0;padding:0;box-sizing:border-box}
  html,body{width:1200px;height:1200px;overflow:hidden}
  body{background:var(--stage);font-family:"Montserrat",sans-serif;position:relative}
  .flyer{position:absolute;left:183px;top:40px;width:834px;height:1120px;background:var(--paper);overflow:hidden}
  .hero-art{position:absolute;left:0;top:0}
  .headline{position:absolute;left:44px;top:26px;line-height:.92;font-weight:800;letter-spacing:-1.5px}
  .headline .line-red{color:var(--red);font-size:49px;display:block}
  .headline .line-navy{color:var(--navy);font-size:76px;display:block;letter-spacing:-2.5px}
  .subtitle{position:absolute;left:45px;top:157px;color:var(--navy);font-weight:700;font-size:22px;line-height:1.1;letter-spacing:-.3px;text-transform:uppercase}
  .tagline{position:absolute;left:45px;top:218px;width:330px;color:var(--ink);font-weight:500;font-size:15.5px;line-height:1.3;text-transform:uppercase;letter-spacing:-.3px}
  .block{position:absolute;left:45px;font-weight:800;letter-spacing:-1px;text-transform:uppercase}
  .block .red{color:var(--red)}
  .block .navy{color:var(--navy)}
  .when{top:280px}
  .when .city{font-size:37px;line-height:1}
  .when .day{font-size:46px;line-height:1;margin-top:2px}
  .when .rule,.start .rule{height:2px;background:var(--navy);margin:5px 0 4px}
  .when .rule{width:240px}
  .when .session{font-size:25px;font-weight:700;letter-spacing:-.6px}
  .start{top:428px}
  .start .label{font-size:40px;line-height:1}
  .start .date{font-size:47px;line-height:1;margin-top:-2px;letter-spacing:-2px}
  .start .rule{width:200px}
  .start .note{font-size:22px;font-weight:700;line-height:1.02;letter-spacing:-.7px}
  .badge{position:absolute;left:614px;top:488px;width:156px;height:202px}
  .badge-text{position:absolute;left:632px;top:510px;width:128px;color:#fff;font-weight:800;font-size:27px;line-height:1.02;letter-spacing:-1px;text-transform:uppercase}
  .audience{position:absolute;left:0;width:834px;top:683px;text-align:center;font-weight:700;font-size:15px;color:var(--ink);letter-spacing:-.3px;text-transform:uppercase}
  .topics-title{position:absolute;left:0;width:834px;top:702px;text-align:center;font-weight:800;font-size:24px;color:var(--red);letter-spacing:-.5px;text-transform:uppercase}
  .topic{position:absolute;width:160px;margin-left:-80px;text-align:center}
  .topic .ring{width:80px;height:80px;margin:0 auto;border-radius:50%;background:#fff;border:2px solid var(--icon-ring);box-shadow:0 2px 6px rgba(0,0,0,.08);display:flex;align-items:center;justify-content:center}
  .topic .name{margin-top:6px;color:var(--label);font-size:15.5px;line-height:1.05;font-weight:500;text-transform:uppercase;letter-spacing:-.4px}
  .topic svg{width:50px;height:50px;fill:none;stroke-width:2;stroke-linecap:round;stroke-linejoin:round}
  .n{stroke:var(--navy)} .r{stroke:var(--red)}
</style>
</head>
<body>
<main class="flyer">
  <svg class="hero-art" width="834" height="660" viewBox="0 0 834 660">
    <defs>
      <linearGradient id="interiorFade" x1="0" y1="0" x2="1" y2="0">
        <stop offset="0" stop-color="#f0f0f0"/>
        <stop offset="1" stop-color="#dcdcdc"/>
      </linearGradient>
      <linearGradient id="familyTone" x1="0" y1="0" x2="0" y2="1">
        <stop offset="0" stop-color="#ece9e4"/>
        <stop offset=".5" stop-color="#d9b98a"/>
        <stop offset="1" stop-color="#d8d2ca"/>
      </linearGradient>
    </defs>
    <g role="img" aria-label="Faded photo of a bright modern interior">
      <polygon points="0,0 590,0 238,636 0,636" fill="url(#interiorFade)" opacity=".55"/>
      <polygon points="0,320 400,320 238,636 0,636" fill="#ffffff" opacity=".6"/>
    </g>
    <polygon role="img" aria-label="Photo of a smiling family sitting on the floor with arms forming a roof" points="590,0 834,0 834,636 238,636" fill="url(#familyTone)"/>
    <polygon class="accent-stripe" points="571,0 590,0 279,559 260,559" fill="var(--red)"/>
    <polygon class="accent-bar" points="539,636 834,636 834,652 531,652" fill="var(--navy)"/>
  </svg>

  <h1 class="headline"><span class="line-red">REAL ESTATE</span><span class="line-navy">COURSE</span></h1>
  <h2 class="subtitle">Pathways to<br>Brightmoor Land Ventures</h2>
  <p class="tagline">Investing in knowledge is investing in opportunities</p>

  <div class="block when">
    <div class="red city">Alderbrook</div>
    <div class="navy day">10 Tuesday</div>
    <div class="rule"></div>
    <div class="red session">Evenings Sessions</div>
  </div>

  <div class="block start">
    <div class="red label">Starting</div>
    <div class="navy date">Feb.28</div>
    <div class="rule"></div>
    <div class="red note">Limited Partial</div>
    <div class="navy note">Scholarships</div>
  </div>

  <svg class="badge" viewBox="0 0 156 202">
    <polygon points="3,3 153,3 153,199 3,119" fill="var(--red)" stroke="#fff" stroke-width="4"/>
  </svg>
  <div class="badge-text">Early<br>Bird<br>Special</div>

  <p class="audience">For those that started or would like to go into real estate</p>
  <p class="topics-title">Topics: Partial Listing</p>

  <div class="topic" style="left:115px;top:748px">
    <div class="ring"><svg viewBox="0 0 50 50"><path class="n" d="M8 22c0-6 5-9 8-9s8 3 8 9-4 8-8 8-8-2-8-8z M13 13l2-4h2l2 4"/><path class="r" d="M6 44h38M10 44V36M16 44V34M22 44V32M28 44V30M34 44V28M40 44V26M8 34l10-6 8 4 14-10"/><path class="n" d="M30 24V8h8v16M38 14h6v12"/></svg></div>
    <div class="name">Real Estate<br>Investment<br>Strategies</div>
  </div>
  <div class="topic" style="left:268px;top:748px">
    <div class="ring"><svg viewBox="0 0 50 50"><circle class="n" cx="22" cy="20" r="12"/><path class="n" d="M16 16h12M16 21h12M16 26h8"/><path class="n" d="M31 29l12 12"/><circle class="r" cx="12" cy="38" r="5"/></svg></div>
    <div class="name">Due Diligence</div>
  </div>
  <div class="topic" style="left:416px;top:748px">
    <div class="ring"><svg viewBox="0 0 50 50"><path class="n" d="M18 10h8l-3 6c6 3 9 9 9 14 0 8-6 10-10 10s-14-2-14-10c0-5 3-11 9-14z"/><ellipse class="r" cx="37" cy="28" rx="8" ry="3"/><path class="r" d="M29 28v10c0 2 4 3 8 3s8-1 8-3V28M29 33c0 2 4 3 8 3s8-1 8-3"/><circle class="r" cx="26" cy="38" r="6"/></svg></div>
    <div class="name">Financing</div>
  </div>
  <div class="topic" style="left:564px;top:748px">
    <div class="ring"><svg viewBox="0 0 50 50"><rect class="n" x="12" y="8" width="26" height="34"/><path class="n" d="M16 32h18M16 36h18M16 28h10"/><circle class="r" cx="25" cy="18" r="5"/><path class="r" d="M23 18l2 2 3-4"/></svg></div>
    <div class="name">Underwriting</div>
  </div>
  <div class="topic" style="left:714px;top:748px">
    <div class="ring"><svg viewBox="0 0 50 50"><path class="n" d="M22 22l12-12 12 12M26 20v18h16V20"/><rect class="r" x="6" y="24" width="20" height="20"/><path class="r" d="M10 30h12M10 35h12M10 40h8"/></svg></div>
    <div class="name">Property<br>Management</div>
  </div>

  <div class="topic" style="left:115px;top:899px">
    <div class="ring"><svg viewBox="0 0 50 50"><path class="r" d="M6 24L24 8l18 16M10 21v19h12"/><path class="n" d="M26 28l8-8 6 6-8 8zM33 31l10 10"/><path class="n" d="M22 44h14"/></svg></div>
    <div class="name">Real Estate<br>Legal Basics</div>
  </div>
  <div class="topic" style="left:268px;top:899px">
    <div class="ring"><svg viewBox="0 0 50 50"><path class="n" d="M6 24l8-6 8 4 6-2 8-2 8 6-10 12-6-4-6 4z M18 28l6 6M22 26l6 6"/><circle class="r" cx="25" cy="10" r="5"/><path class="r" d="M23 10l2 2 3-4"/></svg></div>
    <div class="name">Sourcing<br>Deals</div>
  </div>
  <div class="topic" style="left:416px;top:899px">
    <div class="ring"><svg viewBox="0 0 50 50"><rect class="r" x="19" y="17" width="12" height="16"/><path class="n" d="M25 4v8M25 38v8M4 25h8M38 25h8M10 10l5 5M40 10l-5 5M10 40l5-5M40 40l-5-5"/></svg></div>
    <div class="name">Syndication</div>
  </div>
  <div class="topic" style="left:564px;top:899px">
    <div class="ring"><svg viewBox="0 0 50 50"><circle class="n" cx="16" cy="14" r="6"/><path class="n" d="M4 40V30c0-5 5-8 12-8s12 3 12 8v10z"/><circle class="r" cx="36" cy="34" r="9"/><path class="r" d="M27 34h18M36 25c-4 5-4 13 0 18M36 25c4 5 4 13 0 18"/><circle class="r" cx="40" cy="14" r="6"/></svg></div>
    <div class="name">Dealing<br>with Brokers</div>
  </div>
  <div class="topic" style="left:714px;top:899px">
    <div class="ring"><svg viewBox="0 0 50 50"><rect class="n" x="14" y="6" width="26" height="36"/><path class="n" d="M18 18h12M18 24h12M18 30h8"/><path class="r" d="M8 10v28"/><circle class="r" cx="38" cy="36" r="6"/></svg></div>
    <div class="name">Property<br>Management</div>
  </div>
</main>
</body>
</html>
```